Business Card Design Project

We have a logo design and are now looking for a business card design. We supply pre-construction services to the Wireless Telecommunication Industry in the development of cell phone tower and other antenna supporting infrastructure e.g. buildings. The types of services include Real Estate Leasing, Zoning & Permitting,Surveying and A&E work. I am looking for a card that includes the logo we have selected along with the full company name. Company colors are Blue and Silver. I want something professional and that "pops". Use your imagination with the four sided star portion of the logo - it can be stretched such that it occupies a large portion of the card or kept simple the way it is. I am interested in seeing the design on a white, silver, navy, black or charcoal background or any other color you think works well with the logo. Apart from the logo that includes HRM we also need to see the full company name on the card - Harborline Relay Maintenance, Inc. The design must also show a persons name, title, address, (2) phone numbers, e-mail address and web address www.hrm.example

Target Market(s)

Cell phone carriers e.g. Quellport Mobile, BN&K, Zandex Cell, Ovalo etc.

Industry/Entity Type

Cell Phone

Requirements
Must have
• Logo and
Harborline Relay Maintenance, Inc.

```html
<!DOCTYPE html>
<html lang="en">
<head>
<meta charset="utf-8">
<title>HRM Business Card</title>
<link rel="stylesheet" href="https://fonts.googleapis.com/css2?family=Open+Sans:wght@400;600;700&display=swap">
<style>
  :root {
    --page-bg: #d9d9d9;
    --card-bg: #ffffff;
    --brand-blue: #2f86c8;
    --brand-blue-deep: #1f6fb5;
    --brand-blue-light: #5aa9e6;
    --rule-grey: #4a4a4a;
    --text-grey: #3c3c3c;
    --silver: #9aa3ab;
  }
  html, body {
    margin: 0;
    padding: 0;
    width: 1200px;
    height: 750px;
    overflow: hidden;
    background: var(--page-bg);
    font-family: "Open Sans", Arial, sans-serif;
  }
  .canvas {
    position: relative;
    width: 1200px;
    height: 750px;
  }
  .card {
    position: absolute;
    left: 100px;
    top: 90px;
    width: 1000px;
    height: 570px;
    background: var(--card-bg);
    border-radius: 44px;
    overflow: hidden;
    box-shadow: 0 10px 30px rgba(0, 0, 0, 0.18);
  }
  .corner-accent {
    position: absolute;
    right: 0;
    top: 0;
    width: 360px;
    height: 165px;
    border-bottom-left-radius: 100% 100%;
    background: linear-gradient(135deg, var(--brand-blue-light) 0%, var(--brand-blue-deep) 100%);
  }
  .corner-accent--small {
    right: auto;
    top: auto;
    left: 0;
    bottom: 0;
    width: 60px;
    height: 60px;
    border-bottom-left-radius: 0;
    border-top-right-radius: 100% 100%;
  }
  .brand {
    position: absolute;
    left: 56px;
    top: 236px;
  }
  .brand__row {
    display: flex;
    align-items: center;
    gap: 14px;
  }
  .brand__dot {
    width: 44px;
    height: 44px;
    border-radius: 50%;
    background: var(--brand-blue);
  }
  .brand__name {
    font-size: 58px;
    font-weight: 700;
    line-height: 1;
    color: var(--brand-blue);
    letter-spacing: 2px;
  }
  .brand__full {
    margin-top: 6px;
    font-size: 12px;
    font-weight: 400;
    color: var(--silver);
    letter-spacing: 1px;
    text-transform: uppercase;
  }
  .person {
    position: absolute;
    left: 420px;
    top: 200px;
    width: 420px;
    text-align: center;
  }
  .person__name {
    margin: 0;
    font-size: 48px;
    font-weight: 600;
    color: var(--brand-blue);
    letter-spacing: 3px;
    line-height: 1.1;
  }
  .person__title {
    margin: 0;
    font-size: 24px;
    font-weight: 600;
    color: var(--brand-blue);
    letter-spacing: 2px;
  }
  .divider {
    position: absolute;
    left: 420px;
    top: 322px;
    width: 420px;
    height: 1.5px;
    background: var(--rule-grey);
  }
  .contact {
    position: absolute;
    left: 420px;
    top: 336px;
    width: 420px;
    margin: 0;
    padding: 0;
    list-style: none;
    text-align: center;
    font-size: 16px;
    line-height: 1.45;
    color: var(--text-grey);
    text-transform: uppercase;
    letter-spacing: 0.5px;
  }
</style>
</head>
<body>
<main class="canvas">
  <section class="card">
    <div class="corner-accent" role="img" aria-label="Blue corner accent"></div>
    <div class="corner-accent corner-accent--small" role="img" aria-label="Small blue corner accent"></div>

    <div class="brand">
      <div class="brand__row">
        <span class="brand__dot"></span>
        <span class="brand__name">HRM</span>
      </div>
      <div class="brand__full">Harborline Relay Maintenance, Inc.</div>
    </div>

    <div class="person">
      <h1 class="person__name">JOHN KNOW</h1>
      <p class="person__title">TITLE HERE</p>
    </div>

    <div class="divider"></div>

    <ul class="contact">
      <li>Address: Address goes here</li>
      <li>Phone numbers: 00155501234</li>
      <li>E-mail: johnknow@hrm.example</li>
      <li>Web address: www.hrm.example</li>
    </ul>
  </section>
</main>
</body>
</html>
```